Need webpage for TUTORING COMPANY

Hello,
Our tutoring company Quillbrook Lessons is launching a new program named 'After School Pick-Up Program'.
We would like a website created to showcase our new program.
Our current company page is: www.quillbrook.org
The new program webpage can have a link on the current company page that takes you to the new program webpage. We are open to ideas in regards to this. I would like the new program page to have the following:
-student online registration
-a way for parents to schedule their calendar days for the program
-a way for parents to pay (pricing is $45 a day or $745 per month)
The web content will be similar to this: http://brightferncarehub.com/
I personally did not like their website and I prefer a modern, sleek, structured, eye catchy design.
We need the website fairly quickly.
Thank you,
Revati Kapoor
P.S: I am attaching the flyer & brochure for the new program.
Industry/Entity Type
School
Logo Text
After School Program by QuillBrook Lessonns
Look and feel

```html
<!DOCTYPE html>
<html lang="en">
<head>
<meta charset="utf-8">
<title>Quillbrook Lessons – After School Pick-Up Program</title>
<link href="https://fonts.googleapis.com/css2?family=Oswald:wght@400;500;700&family=Open+Sans:wght@400;600;700&display=swap" rel="stylesheet">
<style>
:root{
  --ink:#232427;
  --ink-2:#2d2e32;
  --ink-3:#3a3b40;
  --yellow:#f6c319;
  --yellow-dk:#e0ad0a;
  --grey:#ececec;
  --grey-2:#d9d9d9;
  --text:#555;
  --white:#fff;
}
*{box-sizing:border-box;margin:0;padding:0}
html,body{width:1200px;height:2400px;overflow:hidden}
body{font-family:"Open Sans",Arial,sans-serif;color:var(--text);background:var(--white);position:relative}

/* top bar */
.topbar{height:36px;background:#1b1c1e;color:#bbb;font-size:12px;display:flex;align-items:center;justify-content:space-between;padding:0 70px}
.topbar-contact span{margin-right:26px}
.social{display:flex;gap:6px}
.social i{display:block;width:18px;height:18px;background:var(--ink-3);border-radius:2px}

/* nav */
.nav{height:60px;background:var(--ink);display:flex;align-items:center;justify-content:space-between;padding:0 70px;border-bottom:1px solid #333}
.brand{display:flex;align-items:center;gap:10px;color:var(--white);font-family:"Oswald",sans-serif;font-size:24px;font-weight:500;letter-spacing:1px}
.brand i{width:26px;height:26px;background:var(--yellow);display:block}
.menu{display:flex;gap:4px;font-size:13px}
.menu a{color:#ddd;text-decoration:none;padding:20px 16px}
.menu a.active{background:var(--yellow);color:var(--ink)}

/* hero */
.hero{height:360px;background:linear-gradient(135deg,#2b2c30,#1f2023);position:relative;padding:40px 0 0 90px;overflow:hidden}
.hero h1{font-family:"Oswald",sans-serif;font-size:80px;line-height:1;color:var(--white);font-weight:700;letter-spacing:1px}
.hero h2{font-family:"Oswald",sans-serif;font-size:38px;line-height:1.2;color:var(--white);font-weight:400;margin-top:6px}
.hero .tag{display:inline-block;background:var(--yellow);color:var(--ink);font-size:14px;font-weight:700;padding:6px 14px;margin-top:20px}
.hero .limit{color:var(--white);font-size:14px;font-weight:600;margin-top:10px}
.hero .phone{display:inline-block;background:var(--yellow);color:var(--ink);font-family:"Oswald",sans-serif;font-size:22px;line-height:1.3;padding:6px 22px;margin-top:10px}
.hero .art{position:absolute;right:60px;top:46px;width:470px;height:260px;border-radius:30px 60px 20px 20px;background:linear-gradient(160deg,#f9cf2a,#e2a80b)}

/* features */
.features{height:200px;background:var(--grey);display:flex;justify-content:center}
.feature{width:260px;display:flex;flex-direction:column;align-items:center;justify-content:center;gap:18px;border-right:1px solid var(--grey-2)}
.feature:last-child{border-right:none}
.feature span{font-family:"Oswald",sans-serif;font-size:15px;color:var(--ink);text-transform:uppercase}

/* mission */
.mission{height:340px;padding:46px 90px 0;display:flex;gap:60px}
.section-title{font-family:"Oswald",sans-serif;font-size:32px;color:var(--ink);text-transform:uppercase;font-weight:500}
.section-title b{color:var(--yellow);font-weight:500}
.rule{width:60px;height:3px;background:var(--yellow);margin:8px 0 18px}
.mission p{font-size:13px;line-height:1.75;width:560px}
.mission .art{width:300px;height:250px;border-radius:50%;background:radial-gradient(circle,#f4f4f4 30%,#f6c319 31%,#e7b20e 60%,#fff 61%)}

/* classes */
.classes{height:440px;background:radial-gradient(ellipse at center,#3a3b3f,#1e1f22);position:relative;padding-top:50px}
.ribbon{width:300px;margin:0 auto;background:var(--yellow);color:var(--ink);text-align:center;font-family:"Oswald",sans-serif;font-size:22px;padding:8px 0;text-transform:uppercase;position:relative}
.ribbon:before,.ribbon:after{content:"";position:absolute;top:0;border:22px solid var(--yellow-dk)}
.ribbon:before{left:-30px;border-left-color:transparent}
.ribbon:after{right:-30px;border-right-color:transparent}
.screens{display:flex;justify-content:center;gap:140px;margin-top:48px}
.screen{width:340px}
.screen .bar{height:14px;background:linear-gradient(#999,#666);border-radius:7px}
.screen .sheet{background:var(--white);margin:0 14px;height:220px;padding:26px 30px;text-align:center;box-shadow:0 6px 16px rgba(0,0,0,.4)}
.screen h3{font-size:14px;color:#444;font-weight:600}
.screen h4{font-family:"Oswald",sans-serif;font-size:16px;color:var(--ink);margin:4px 0 16px;font-weight:500}
.screen li{list-style:none;font-size:12px;line-height:2;text-align:left}

/* pay & dates */
.booking{height:500px;padding:40px 90px 0;display:flex;justify-content:space-between}
.plans{display:flex;gap:18px;margin-top:6px}
.plan{width:205px;background:var(--yellow);text-align:center}
.plan .ph{background:var(--ink);color:var(--white);font-size:14px;font-weight:600;padding:12px 0}
.plan .price{width:104px;height:104px;border-radius:50%;background:var(--ink);color:var(--white);margin:18px auto 14px;display:flex;flex-direction:column;justify-content:center;font-family:"Oswald",sans-serif}
.plan .price strong{font-size:36px;line-height:1}
.plan .price small{font-size:11px}
.plan ul{background:var(--white);padding:12px 18px;text-align:left;border:1px solid var(--grey-2)}
.plan li{list-style:none;font-size:12px;line-height:2.1;border-bottom:1px solid #eee;display:flex;gap:8px;align-items:center}
.plan li:last-child{border:none}
.plan .btn{display:block;background:var(--ink);color:var(--white);font-family:"Oswald",sans-serif;font-size:16px;padding:11px 0}
.dots{display:flex;flex-direction:column;gap:18px;margin-top:80px}
.dots i{width:30px;height:30px;border-radius:50%;background:var(--ink);display:block;border:3px solid var(--grey-2)}
.dots i.on{background:var(--yellow)}
.cal{width:400px;background:var(--ink);margin-top:6px;color:#ccc}
.cal .ch{display:flex;justify-content:space-between;padding:12px 16px;font-size:14px;color:var(--white);border-bottom:1px solid #444}
.cal table{width:100%;border-collapse:collapse;font-size:12px;text-align:center}
.cal th{color:var(--yellow);font-weight:600;padding:8px 0}
.cal td{padding:7px 0}
.cal td.sel{background:var(--yellow);color:var(--ink);font-weight:700}
.cal .foot{background:var(--white);color:var(--ink);padding:14px 16px;border:1px solid var(--grey-2)}
.cal .foot p{font-size:13px;font-weight:600}
.cal .foot small{font-size:11px;color:#777}
.cal .submit{display:block;margin:12px auto 0;width:120px;text-align:center;background:var(--yellow);font-size:13px;font-weight:600;padding:7px 0}

/* contact */
.contact-section{height:330px;background:#2a2b2e;position:relative;padding-top:44px;text-align:center;color:#ccc}
.contact-section .map{position:absolute;inset:70px 150px 30px;background:radial-gradient(ellipse,#38393d,#2a2b2e 70%);border-radius:40%}
.contact-section h2{position:relative;font-family:"Oswald",sans-serif;color:var(--white);font-size:30px;font-weight:500}
.contact-section .rule{margin:8px auto 0;position:relative}
.ccols{position:relative;display:flex;justify-content:center;gap:40px;margin-top:46px}
.ccol{width:220px;font-size:12px;line-height:1.7}
.ccol svg{display:block;margin:0 auto 12px}

/* footer */
.footer{height:134px;display:flex;align-items:center;justify-content:space-between;padding:0 90px;border-top:4px solid var(--yellow)}
.footer .brand{color:var(--ink)}
.footer nav{font-size:12px;color:#777;text-align:right;line-height:1.9}
.footer nav a{color:#555;text-decoration:none;margin-left:14px}
</style>
</head>
<body>

<div class="topbar">
  <div class="topbar-contact"><span>+1 555 204 3318</span><span>info@quillbrook.org</span></div>
  <div class="social"><i></i><i></i><i></i><i></i></div>
</div>

<header class="nav">
  <div class="brand"><i></i>QUILLBROOK</div>
  <nav class="menu">
    <a class="active" href="#">Home</a><a href="#">About Us</a><a href="#">Programmes</a><a href="#">Classes</a><a href="#">Calendar</a><a href="#">Contact Us</a>
  </nav>
</header>

<section class="hero">
  <h1>AFTERSCHOOL</h1>
  <h2>PICK UP- PROGRAME</h2>
  <div class="tag">NOW ENROLLING GRADES K-6</div>
  <div class="limit">SPACE IS LIMITED</div>
  <div class="phone">(555) 204-3318</div>
  <div class="art" role="img" aria-label="Yellow school bus with children standing in front"></div>
</section>

<section class="features">
  <div class="feature">
    <svg width="56" height="44" viewBox="0 0 56 44"><rect x="4" y="4" width="48" height="30" rx="5" fill="#232427"/><rect x="9" y="9" width="16" height="11" fill="#ececec"/><rect x="31" y="9" width="16" height="11" fill="#ececec"/><circle cx="14" cy="36" r="5" fill="#232427"/><circle cx="42" cy="36" r="5" fill="#232427"/></svg>
    <span>Pick up from school</span>
  </div>
  <div class="feature">
    <svg width="56" height="44" viewBox="0 0 56 44"><path d="M10 8h30v18a12 12 0 0 1-12 12h-6a12 12 0 0 1-12-12z" fill="#232427"/><path d="M40 12h5a6 6 0 0 1 0 12h-5" stroke="#232427" stroke-width="4" fill="none"/><rect x="6" y="40" width="38" height="3" fill="#232427"/></svg>
    <span>Snack time</span>
  </div>
  <div class="feature">
    <svg width="56" height="44" viewBox="0 0 56 44"><path d="M4 6q12-4 24 4q12-8 24-4v32q-12-4-24 4q-12-8-24-4z" fill="#232427"/><path d="M28 10v32" stroke="#ececec" stroke-width="2"/></svg>
    <span>Home work help</span>
  </div>
  <div class="feature">
    <svg width="56" height="44" viewBox="0 0 56 44"><circle cx="28" cy="22" r="18" fill="none" stroke="#232427" stroke-width="4"/><path d="M28 10v12l8 6" stroke="#232427" stroke-width="4" fill="none"/></svg>
    <span>Enrichment excercise</span>
  </div>
</section>

<section class="mission">
  <div>
    <h2 class="section-title">Our <b>Mission</b></h2>
    <div class="rule"></div>
    <p>Our after school program gives children a safe, warm and structured place to spend the afternoon. We collect each child from school, serve a healthy snack and guide them through their homework with patient tutors. Small groups let every student get the attention they need to grow in confidence.</p>
    <p style="margin-top:12px">Daily enrichment activities keep young minds curious, while parents enjoy peace of mind knowing their children are cared for until pick-up time each evening.</p>
  </div>
  <div class="art" role="img" aria-label="Illustration of children holding hands in a circle"></div>
</section>

<section class="classes">
  <div class="ribbon">Our Classes</div>
  <div class="screens">
    <div class="screen">
      <div class="bar"></div>
      <div class="sheet">
        <h3>Typical Daily Schedule</h3>
        <h4>AFTER SCHOOL PROGRAMME</h4>
        <ul>
          <li>3:15 pm - 3:30 pm &nbsp; Pick up from school</li>
          <li>3:30 pm - 4:00 pm &nbsp; Snack time</li>
          <li>4:00 pm - 5:00 pm &nbsp; Home work help</li>
          <li>5:00 pm - 6:00 pm &nbsp; Enrichment excercise</li>
        </ul>
      </div>
    </div>
    <div class="screen">
      <div class="bar"></div>
      <div class="sheet">
        <h3>Typical Daily Schedule</h3>
        <h4>AFTER SCHOOL PROGRAMME</h4>
        <ul>
          <li>3:15 pm - 3:30 pm &nbsp; Pick up from school</li>
          <li>3:30 pm - 4:00 pm &nbsp; Snack time</li>
          <li>4:00 pm - 5:00 pm &nbsp; Home work help</li>
          <li>5:00 pm - 6:00 pm &nbsp; Enrichment excercise</li>
        </ul>
      </div>
    </div>
  </div>
</section>

<section class="booking">
  <div>
    <h2 class="section-title">How to <b>Pay Parents</b></h2>
    <div class="rule"></div>
    <div class="plans">
      <div class="plan">
        <div class="ph">Per Day Package</div>
        <div class="price"><strong>$45</strong><small>per day</small></div>
        <ul>
          <li><svg width="10" height="10"><path d="M1 5l3 3 5-7" stroke="#f6c319" stroke-width="2" fill="none"/></svg>School pick up</li>
          <li><svg width="10" height="10"><path d="M1 5l3 3 5-7" stroke="#f6c319" stroke-width="2" fill="none"/></svg>Healthy snack</li>
          <li><svg width="10" height="10"><path d="M1 5l3 3 5-7" stroke="#f6c319" stroke-width="2" fill="none"/></svg>Homework help</li>
          <li><svg width="10" height="10"><path d="M1 5l3 3 5-7" stroke="#f6c319" stroke-width="2" fill="none"/></svg>Enrichment time</li>
        </ul>
        <a class="btn">GET STARTED</a>
      </div>
      <div class="plan">
        <div class="ph">Monthly Package</div>
        <div class="price"><strong>$745</strong><small>per month</small></div>
        <ul>
          <li><svg width="10" height="10"><path d="M1 5l3 3 5-7" stroke="#f6c319" stroke-width="2" fill="none"/></svg>School pick up</li>
          <li><svg width="10" height="10"><path d="M1 5l3 3 5-7" stroke="#f6c319" stroke-width="2" fill="none"/></svg>Healthy snack</li>
          <li><svg width="10" height="10"><path d="M1 5l3 3 5-7" stroke="#f6c319" stroke-width="2" fill="none"/></svg>Homework help</li>
          <li><svg width="10" height="10"><path d="M1 5l3 3 5-7" stroke="#f6c319" stroke-width="2" fill="none"/></svg>Enrichment time</li>
        </ul>
        <a class="btn">GET STARTED</a>
      </div>
    </div>
  </div>
  <div class="dots"><i class="on"></i><i></i><i></i></div>
  <div>
    <h2 class="section-title">Select your <b>dates for classes</b></h2>
    <div class="rule"></div>
    <div class="cal">
      <div class="ch"><span>&#8249;</span><span>September</span><span>&#8250;</span></div>
      <table>
        <tr><th>Su</th><th>Mo</th><th>Tu</th><th>We</th><th>Th</th><th>Fr</th><th>Sa</th></tr>
        <tr><td></td><td></td><td></td><td></td><td>1</td><td>2</td><td>3</td></tr>
        <tr><td>4</td><td>5</td><td>6</td><td>7</td><td>8</td><td>9</td><td>10</td></tr>
        <tr><td>11</td><td>12</td><td>13</td><td>14</td><td class="sel">15</td><td>16</td><td>17</td></tr>
        <tr><td>18</td><td>19</td><td>20</td><td>21</td><td>22</td><td>23</td><td>24</td></tr>
        <tr><td>25</td><td>26</td><td>27</td><td>28</td><td>29</td><td>30</td><td></td></tr>
      </table>
      <div class="foot">
        <p>September - Thursday 15 TH</p>
        <small>Pick up and homework session booked</small>
        <span class="submit">Submit</span>
      </div>
    </div>
  </div>
</section>

<section class="contact-section">
  <div class="map" role="img" aria-label="Faint world map background"></div>
  <h2>CONTACT US</h2>
  <div class="rule"></div>
  <div class="ccols">
    <div class="ccol">
      <svg width="26" height="34" viewBox="0 0 26 34"><rect x="3" y="1" width="20" height="32" rx="3" fill="#f6c319"/><rect x="6" y="5" width="14" height="20" fill="#2a2b2e"/></svg>
      (555) 204-3318 · (555) 204-3319<br>Mon – Fri, 8am – 6pm
    </div>
    <div class="ccol">
      <svg width="26" height="34" viewBox="0 0 26 34"><path d="M13 33C4 20 1 15 1 12a12 12 0 0 1 24 0c0 3-3 8-12 21z" fill="#f6c319"/><circle cx="13" cy="12" r="4" fill="#2a2b2e"/></svg>
      48 Fernhill Road, Suite 2<br>Westbury, Main Office
    </div>
    <div class="ccol">
      <svg width="34" height="34" viewBox="0 0 34 34"><rect x="2" y="8" width="30" height="18" rx="4" fill="#f6c319"/><circle cx="9" cy="28" r="4" fill="#f6c319"/><circle cx="25" cy="28" r="4" fill="#f6c319"/></svg>
      Pick up from partner schools<br>within five miles
    </div>
    <div class="ccol">
      <svg width="34" height="34" viewBox="0 0 34 34"><path d="M2 16L32 2 24 32 16 20z" fill="#f6c319"/></svg>
      info@quillbrook.org<br>www.quillbrook.org
    </div>
  </div>
</section>

<footer class="footer">
  <div class="brand"><i></i>QUILLBROOK</div>
  <nav>
    <div><a href="#">Home</a><a href="#">About Us</a><a href="#">Programmes</a><a href="#">Classes</a><a href="#">Calendar</a><a href="#">Contact Us</a></div>
    <div>© QuillBrook Lessonns. All rights reserved.</div>
  </nav>
</footer>

</body>
</html>
```